Flyer for American Indian Elders on Dementia Warning Signs

We need a flyer designed for older adults who are American Indian or Alaska Native (in the U.S.).

Ideally, the flyer should complement the colors of our logos. The project logo and our organization logo are attached to the brief.

When people see the flyer we want them to feel that it represents their culture, is warm, and professional but relatable to older adults and people who have limited incomes.

I have attached an earlier draft of the document we designed ourselves BUT we want different and better.

It is for older adults who have trouble reading so:
1. you must use a font that is 11.5 points or larger
2. Do not put text over complex pictures or use shading with words
3. You can use a serif font for the heading, but should use san serif for the body text
4. There should be good contrast between the font color and background

Please do not use any images that include a head dress or pictures of American Indian people or things that are very traditional or "token" imagery.

We need to save a small space under the call out box/ somewhere on the flyer for other people to add their logo once they download.

Let us know if you have questions or need additional information.

Target Market(s)

Older American Indian people

Font styles to use
Serif
Sans Serif

Requirements
Must have
• Easy to read for older adults
Should not have
• indian headdress

```html
<!DOCTYPE html>
<html lang="en">
<head>
<meta charset="utf-8">
<title>10 Signs of Thinking or Memory Changes That Might Be Dementia</title>
<link rel="stylesheet" href="https://fonts.googleapis.com/css2?family=Barlow+Condensed:wght@700;800&family=Lato:wght@400;700;900&display=swap">
<style>
  :root{
    --red:#b0534d;
    --red-soft:#f1d4d3;
    --teal:#5db5be;
    --teal-deep:#4aa3ad;
    --aqua:#86dce4;
    --blue-soft:#d9e6e8;
    --slate:#6f8f93;
    --ink:#1f1f1f;
    --paper:#ffffff;
    --bg:#ffffff;
  }
  *{box-sizing:border-box;margin:0;padding:0}
  html,body{width:885px;height:1200px;overflow:hidden;background:var(--bg)}
  body{font-family:"Lato",Arial,sans-serif;color:var(--ink)}
  .flyer{position:absolute;left:63px;top:64px;width:760px;height:1073px;background:var(--paper);box-shadow:0 2px 8px rgba(0,0,0,.22);overflow:hidden}

  .masthead{position:absolute;left:0;top:0;width:520px;height:112px}
  .masthead svg{position:absolute;inset:0}
  .masthead-band{position:absolute;left:0;top:97px;width:497px;height:13px;background:linear-gradient(90deg,#c08c88,#b86f69)}
  .masthead h1{position:absolute;left:16px;top:17px;width:430px;font-family:"Barlow Condensed","Arial Narrow",sans-serif;font-weight:800;font-size:29px;line-height:29px;color:#fff;text-transform:uppercase;letter-spacing:0;white-space:nowrap}

  .org{position:absolute;left:492px;top:26px;width:260px;height:64px;display:flex;align-items:center;gap:10px}
  .org-dot{flex:0 0 58px;height:58px;border-radius:50%;border:4px solid var(--teal)}
  .org-name{font-weight:900;font-size:15px;line-height:17px;color:var(--teal-deep);text-transform:uppercase}

  .intro{position:absolute;left:14px;top:124px;width:732px;font-size:13.4px;line-height:17px}
  .intro p+p{margin-top:10px}
  .intro strong{font-weight:900}

  .sign{position:absolute;left:0;width:495px;padding:10px 8px 0 58px;border-bottom:3px solid var(--red);background:var(--red-soft)}
  .sign.cool{background:var(--blue-soft);border-bottom-color:var(--teal)}
  .sign-num{position:absolute;left:14px;top:10px;width:33px;height:33px;border-radius:50%;background:#fff;border:2px solid var(--red);box-shadow:1px 2px 2px rgba(0,0,0,.25);font-family:"Barlow Condensed",sans-serif;font-weight:800;font-size:21px;line-height:29px;text-align:center;color:#1a1a1a}
  .sign-head{font-size:13.6px;line-height:17px;font-weight:400;text-transform:uppercase}
  .sign-head b{font-weight:900;letter-spacing:-.2px}
  .sign-text{font-size:13.6px;line-height:18px}
  .sign-list{list-style:none;font-size:13.4px;line-height:20px;margin-top:3px}
  .sign-list li::before{content:"\2022";margin-right:3px}
  .sign-list.row{display:flex;gap:36px}

  .points{position:absolute;left:509px;top:220px;width:251px;height:407px}
  .points-frame{position:absolute;inset:0;background:linear-gradient(135deg,#a06a66,#8d8486)}
  .points-body{position:absolute;left:13px;top:13px;right:0;bottom:13px;background:var(--aqua)}
  .points-tab{position:absolute;left:57px;top:0;width:150px;height:27px;border-radius:0 0 14px 14px;background:var(--red);border:3px solid #fff;border-top:none;color:#fff;font-weight:900;font-size:15px;line-height:26px;text-align:center}
  .point{position:absolute;left:20px;right:0;padding:2px 8px 6px 8px;border-left:2px solid #2b2b2b;border-bottom:1px solid #2b2b2b;font-size:13.4px;line-height:17px;color:#1b1b1b}

  .partner{position:absolute;left:515px;top:676px;width:238px;text-align:center}
  .partner-dot{width:62px;height:62px;border-radius:50%;background:var(--teal);margin:0 auto 14px}
  .partner-name{font-family:"Barlow Condensed",sans-serif;font-weight:800;font-size:24px;line-height:24px;color:var(--red);text-transform:uppercase}
  .learn{position:absolute;left:515px;top:842px;width:238px;text-align:center}
  .learn-lead{font-size:10.8px;line-height:13px;font-weight:700;text-transform:uppercase}
  .learn-who{font-size:16.5px;line-height:18px;font-weight:700;margin-top:6px}
  .link{display:block;margin:6px auto 0;background:var(--red);color:#fff;border-radius:5px;font-weight:700;font-size:13px;line-height:21px;letter-spacing:.3px}
  .link.wide{width:208px}
  .link.narrow{width:176px}
  .logo-space{position:absolute;left:515px;top:983px;width:238px;height:82px;border:1.5px dashed var(--red)}
</style>
</head>
<body>
<main class="flyer">
  <header class="masthead">
    <svg width="520" height="112" viewBox="0 0 520 112" aria-hidden="true">
      <defs>
        <linearGradient id="bandFill" x1="0" y1="0" x2="0" y2="1">
          <stop offset="0" stop-color="#6f8f93"/>
          <stop offset=".6" stop-color="#9f6762"/>
          <stop offset="1" stop-color="#a8574f"/>
        </linearGradient>
      </defs>
      <path d="M0 0 H463 Q 452 50 500 110 H0 Z" fill="url(#bandFill)"/>
      <path d="M467 0 Q 456 50 504 110" fill="none" stroke="#5db5be" stroke-width="5"/>
    </svg>
    <div class="masthead-band" role="img" aria-label="Woven band pattern"></div>
    <h1>10 Signs of Thinking or Memory<br>Changes That Might Be Dementia</h1>
  </header>

  <div class="org">
    <span class="org-dot"></span>
    <span class="org-name">Riverstone Resource Center for Brain Health</span>
  </div>

  <section class="intro">
    <p>As we get older, we may slow down a bit. This is a normal part of aging. Changes in memory or thinking that make it harder to get through the day, are not a normal part of aging. These may be early signs of dementia.</p>
    <p>Because American Indian &amp; Alaska Native people have a high risk of dementia, it is important to know the warning signs. <strong>DO YOU HAVE ANY OF THESE 10 SIGNS? IF SO, TALK TO YOUR DOCTOR.</strong></p>
  </section>

  <section class="sign" style="top:229px;height:76px">
    <span class="sign-num">1</span>
    <p class="sign-head"><b>Memory loss that affects your daily life.</b> You may:</p>
    <ul class="sign-list">
      <li style="display:inline-block;width:244px">Forget events or important dates</li><li style="display:inline-block">Repeat yourself</li>
      <li>Rely more often on lists or sticky notes to remember things</li>
    </ul>
  </section>

  <section class="sign cool" style="top:312px;height:76px">
    <span class="sign-num">2</span>
    <p class="sign-head"><b>Trouble planning or solving problems.</b> You may have a harder time:</p>
    <ul class="sign-list row" style="margin-top:6px"><li>Paying bills</li><li>Cooking recipes you have used for years</li></ul>
  </section>

  <section class="sign" style="top:396px;height:41px">
    <span class="sign-num" style="top:4px">3</span>
    <p class="sign-head" style="margin-top:2px"><b>Get confused about the time, date, or where you are</b></p>
  </section>

  <section class="sign cool" style="top:444px;height:61px">
    <span class="sign-num">4</span>
    <p class="sign-head"><b>4.&nbsp;&nbsp; Daily tasks are getting harder</b>, including:</p>
    <ul class="sign-list row" style="margin-top:4px"><li>Driving</li><li>Making a grocery list or going shopping</li></ul>
  </section>

  <section class="sign" style="top:514px;height:95px">
    <span class="sign-num" style="top:16px">5</span>
    <p class="sign-head"><b>Trouble with how your eyesight and thinking work together that gets worse.</b> This includes:</p>
    <ul class="sign-list" style="margin-top:5px"><li>Tripping, falls, or problems with your balance</li><li>Spilling or dropping things more</li></ul>
  </section>

  <section class="sign cool" style="top:617px;height:76px">
    <span class="sign-num" style="top:16px">6</span>
    <p class="sign-text"><b style="font-weight:900">NEW TROUBLE TALKING / WRITING.</b> You have a hard time finding the words you want to say. For example, you may say “that thing on your wrist that tells time” instead of “watch.”</p>
  </section>

  <section class="sign" style="top:701px;height:78px">
    <span class="sign-num" style="top:12px">7</span>
    <p class="sign-head"><b>Lose and cannot find things.</b> For example, you:</p>
    <ul class="sign-list" style="margin-top:5px"><li>Can’t find the coffee pot that you use every day</li><li>Might put your car keys in the freezer</li></ul>
  </section>

  <section class="sign cool" style="top:787px;height:78px">
    <span class="sign-num" style="top:12px">8</span>
    <p class="sign-head"><b>Notice changes in mood / personality.</b> Such as being:</p>
    <ul class="sign-list" style="margin-top:5px"><li>Easily mad or sad in everyday situations</li><li>More fearful (scared) or suspicious (not trusting)</li></ul>
  </section>

  <section class="sign" style="top:873px;height:115px">
    <span class="sign-num" style="top:14px">9</span>
    <p class="sign-head"><b>Act different and make poor choices.</b> This may make you more likely to:</p>
    <ul class="sign-list" style="margin-top:5px"><li>Spend money you do not have or be a scam victim</li><li>Forget to take care of your pet</li><li>Stop washing up regularly or pay less attention to how you look</li></ul>
  </section>

  <section class="sign cool" style="top:995px;height:71px">
    <span class="sign-num" style="font-size:19px">10</span>
    <p class="sign-text"><b style="font-weight:900">PULL AWAY FROM FRIENDS &amp; FAMILY BECAUSE IT IS HARDER TO KEEP UP.</b> You may not want to do things you used to enjoy, like sporting events, church, music, or sex.</p>
  </section>

  <aside class="points">
    <div class="points-frame" role="img" aria-label="Woven pattern frame"></div>
    <div class="points-body"></div>
    <div class="points-tab">MAIN POINTS</div>
    <p class="point" style="top:64px">American Indian &amp; Alaska Native people have a high risk of dementia.</p>
    <p class="point" style="top:136px">Big changes in memory or thinking that make it hard to get through the day are not a normal part of aging.</p>
    <p class="point" style="top:222px">People with one or more of these 10 signs should talk to their doctor to find the cause. It is not always dementia.</p>
    <p class="point" style="top:326px">Early dementia diagnosis gives you a chance to get care and plan your future.</p>
  </aside>

  <div class="partner">
    <div class="partner-dot"></div>
    <p class="partner-name">Kinship Network for Elder Wellness</p>
  </div>

  <div class="learn">
    <p class="learn-lead">To learn more about the warning signs of dementia in</p>
    <p class="learn-who">American Indian and Alaska Native people visit:</p>
    <span class="link wide">www.riverstonebrainhealth.org</span>
    <span class="link narrow">www.elderwellnessinfo.org</span>
  </div>

  <div class="logo-space" aria-label="Space for partner logo"></div>
</main>
</body>
</html>
```